New Construction company looking for powerful bold logo. people see the logo, leaves an impression

We need a business card for our new company. We provide site work for commercial projects in South Texas. We clear land, excavation, run under ground utilities, concrete work, dirt work etc. We like the black card. I created a webpage www.tarn-vbuilders.com .... As I grow with projects I will put up pictures with video, and intro music. Want it look cool, bold, powerful, and slick looking. Creating 'TVB'....as my logo (possibly or if you have something you want to have fun with). Just have fun!!....thank you!

Dorian Pruett Business Manager Serving Ashby County PO Box 4837 Robstown,WD. 40215 Mobile: 361-752-6083 www.tarn-vbuilders.com dorian@tarn-vbuilders.com you can put this anyway you see fit in your design and layout. thank you

Target Market(s)

General Contractors; Home Builders;

Industry/Entity Type

Construction

Contact Information for Business Card

I want the card to be black.

Font styles to use
Other font styles liked:
• Designer choice

Requirements
Must have
• Tarn-V Construction
• Site Work - Utilities/Concrete/Pad/Grading/Excavation (on the back side)
Nice to have
• Maybe TVB as the logo.....or just a symbol that would be TV.....and then construction to tie it togther...

```html
<!DOCTYPE html>
<html lang="en">
<head>
<meta charset="utf-8">
<title>Tarn-V Construction — Business Card</title>
<link rel="stylesheet" href="https://fonts.googleapis.com/css2?family=Open+Sans:wght@400;600;700;800&display=swap">
<style>
  :root {
    --stage: #ecebe8;
    --card-black: #111111;
    --card-white: #ffffff;
    --brand-red: #b3262b;
    --ink: #1c1c1c;
    --ink-soft: #333333;
    --on-dark: #f2f2f2;
  }
  * { box-sizing: border-box; margin: 0; padding: 0; }
  html, body {
    width: 1200px; height: 900px; overflow: hidden;
    background: var(--stage);
    font-family: "Open Sans", Arial, sans-serif;
  }
  .canvas { position: relative; width: 1200px; height: 900px; }

  .card {
    position: absolute;
    width: 600px; height: 343px;
    border-radius: 4px;
    box-shadow: 0 10px 26px rgba(0,0,0,.18);
    overflow: hidden;
  }

  /* Back side */
  .card-back {
    left: 520px; top: 70px;
    background: var(--card-black);
    color: var(--on-dark);
    text-align: center;
  }
  .back-mark {
    position: absolute; left: 0; right: 0; top: 70px;
    display: flex; align-items: center; justify-content: center; gap: 14px;
  }
  .back-mark .dot {
    width: 22px; height: 22px; border-radius: 50%; background: var(--on-dark);
  }
  .back-mark .name {
    font-size: 48px; font-weight: 800; letter-spacing: 1px; color: var(--on-dark);
  }
  .back-title {
    position: absolute; left: 0; right: 0; top: 200px;
    font-size: 17px; font-weight: 400; letter-spacing: .5px;
  }
  .back-services {
    position: absolute; left: 0; right: 0; top: 228px;
    font-size: 17px; font-weight: 400; letter-spacing: .3px;
  }

  /* Front side */
  .card-front {
    left: 80px; top: 450px;
    background: var(--card-white);
    color: var(--ink);
  }
  .front-shapes { position: absolute; inset: 0; }
  .person {
    position: absolute; left: 86px; top: 24px;
  }
  .person .name { font-size: 17px; font-weight: 700; color: var(--brand-red); line-height: 1.1; }
  .person .role { font-size: 13px; font-weight: 400; color: var(--ink-soft); }
  .address {
    position: absolute; left: 40px; top: 120px;
    font-size: 14px; line-height: 1.3; color: var(--ink-soft);
  }
  .contact-list {
    position: absolute; left: 40px; top: 196px;
    list-style: none; font-size: 14px; line-height: 1.5; color: var(--ink);
  }
  .contact-list li { display: flex; align-items: center; gap: 8px; }
  .contact-list svg { width: 12px; height: 12px; flex: none; }
  .front-mark {
    position: absolute; left: 330px; top: 118px; width: 250px;
    display: flex; align-items: center; gap: 10px;
  }
  .front-mark .dot { width: 20px; height: 20px; border-radius: 50%; background: var(--brand-red); flex: none; }
  .front-mark .name {
    font-size: 30px; font-weight: 800; line-height: 1.05; color: var(--brand-red);
  }
</style>
</head>
<body>
<main class="canvas">

  <section class="card card-back" aria-label="Card back">
    <div class="back-mark">
      <span class="dot"></span>
      <span class="name">Tarn-V</span>
    </div>
    <p class="back-title">SITE WORK</p>
    <p class="back-services">Utilities | Concrete | Pad | Grading | Excavation</p>
  </section>

  <section class="card card-front" aria-label="Card front">
    <svg class="front-shapes" viewBox="0 0 600 343" preserveAspectRatio="none" aria-hidden="true">
      <polygon points="0,0 70,0 70,50 0,50" fill="var(--brand-red)"/>
      <polygon points="40,0 70,0 40,35" fill="#ffffff" opacity=".9"/>
      <polygon points="0,258 600,318 600,343 0,343" fill="var(--brand-red)"/>
      <polygon points="250,283 262,284 250,296 238,295" fill="#ffffff"/>
    </svg>

    <div class="person">
      <p class="name">Dorian Pruett</p>
      <p class="role">Business Manager</p>
    </div>

    <p class="address">Serving Ashby County<br>PO Box 4837 Calder Flats,<br>WD. 40215</p>

    <ul class="contact-list">
      <li>
        <svg viewBox="0 0 12 12"><rect x="3" y="0.5" width="6" height="11" rx="1.2" fill="var(--brand-red)"/><rect x="4" y="2" width="4" height="7" fill="#fff"/></svg>
        361-752-6083
      </li>
      <li>
        <svg viewBox="0 0 12 12"><rect x="0.5" y="2" width="11" height="8" fill="var(--brand-red)"/><polyline points="0.5,2 6,7 11.5,2" fill="none" stroke="#fff" stroke-width="1"/></svg>
        dorian@tarn-vbuilders.com
      </li>
      <li>
        <svg viewBox="0 0 12 12"><circle cx="6" cy="6" r="5.5" fill="var(--brand-red)"/><path d="M.5 6h11M6 .5c-3 3-3 8 0 11M6 .5c3 3 3 8 0 11" fill="none" stroke="#fff" stroke-width=".8"/></svg>
        www.tarn-vbuilders.com
      </li>
    </ul>

    <div class="front-mark">
      <span class="dot"></span>
      <span class="name">Tarn-V Construction</span>
    </div>
  </section>

</main>
</body>
</html>
```